business cards, stationary, email signature
Professional
Greta Volsky
President
Corporate office:
3620 E Tamsin Road, Orange, CA 92814
Other locations in San Diego, CA and Reno, NV
greta@farwellgrp.net
www.farwellgrp.net
482650, K, D74
*8(a), *SDB, *SBE, *MBE, *DBE, *CBE
these certifications should be listed in the middle, bottom of the card.
■221119 – Other Electric Power Generation
■236210 – Industrial Building Construction
■236220 – Commercial and Institutional Building Construction
■237310 – Highway, Street, and Bridge Construction
■238160 – Roofing Contractors
■238170 – Siding Contractors
■238220 – Plumbing, Heating, and Air-Conditioning Contractors
■238310 – Drywall and Insulation Contractors
■238320 – Painting and Wall Covering Contractors
■238340 – Tile and Terrazzo Contractors
■238350 – Finish Carpentry Contractors
■238390 – Other Building Finishing Contractors
■238910 – Site Preparation Contractors
■238990 – All Other Specialty Trade Contractors
■541350 – Building Inspection Services
■561210 – Facilities Support Services
■561790 – Other Services to Buildings and Dwellings

```html
<!DOCTYPE html>
<html lang="en">
<head>
<meta charset="utf-8">
<title>Farwell Group — Stationery Options</title>
<link href="https://fonts.googleapis.com/css2?family=Cinzel:wght@600&family=Open+Sans:wght@400;600;700&display=swap" rel="stylesheet">
<style>
  :root {
    --stage: #3a3a3a;
    --ink: #111111;
    --paper: #ffffff;
    --blue: #2f8fd6;
    --blue-dark: #1b3f73;
    --sky: #cfe6f7;
    --sun: #f3c35a;
    --rule: #9a9a9a;
    --text: #333333;
    --muted: #777777;
    --flap: #2b2b2b;
  }
  * { box-sizing: border-box; margin: 0; padding: 0; }
  html, body { width: 1200px; height: 540px; overflow: hidden; background: var(--stage); }
  body { position: relative; font-family: "Open Sans", Arial, sans-serif; color: var(--text); }

  .sheet { position: absolute; background: var(--paper); width: 310px; height: 432px; top: 48px; }
  .sheet--one { left: 52px; }
  .sheet--two { left: 410px; }
  .sheet__header { height: 30px; background: var(--ink); display: flex; align-items: center; justify-content: space-between; padding: 0 10px; }
  .brand { display: flex; align-items: center; gap: 5px; color: var(--paper); font-family: "Cinzel", Georgia, serif; font-size: 9px; font-weight: 600; letter-spacing: .5px; }
  .brand__dot { width: 14px; height: 14px; border-radius: 50%; background: var(--blue); }
  .contact-mini { font-size: 4px; line-height: 6px; color: #dddddd; text-align: right; }
  .sheet__footer { position: absolute; left: 0; right: 0; bottom: 0; height: 20px; background: linear-gradient(90deg, var(--blue-dark), var(--blue)); display: flex; align-items: center; justify-content: space-around; font-size: 4.5px; color: var(--paper); }
  .watermark { position: absolute; border-radius: 50%; background: radial-gradient(circle, var(--sky) 0%, rgba(243,195,90,.25) 55%, rgba(255,255,255,0) 72%); opacity: .6; }
  .sheet--one .watermark { width: 190px; height: 190px; left: 60px; top: 150px; }
  .sheet--two .watermark { width: 60px; height: 60px; right: 14px; bottom: 28px; }

  .fax__title { position: absolute; left: 22px; top: 60px; font-size: 17px; font-weight: 600; color: var(--ink); }
  .fax__rule { position: absolute; left: 22px; right: 22px; top: 84px; border-top: 1px solid var(--rule); }
  .fax__fields { position: absolute; left: 22px; right: 22px; top: 92px; display: grid; grid-template-columns: 1fr 1fr; column-gap: 12px; row-gap: 7px; font-size: 4.5px; color: var(--muted); }
  .fax__field { border-bottom: 1px solid #cccccc; padding-bottom: 2px; }
  .fax__checks { position: absolute; left: 22px; right: 22px; top: 312px; display: flex; justify-content: space-between; font-size: 4.5px; color: var(--muted); }
  .fax__check { display: flex; align-items: center; gap: 3px; }
  .fax__check::before { content: ""; width: 6px; height: 6px; border: 1px solid var(--rule); }

  .label { position: absolute; top: 498px; font-size: 20px; color: var(--paper); }
  .label--one { left: 168px; }
  .label--two { left: 520px; }

  .envelope { position: absolute; left: 763px; width: 413px; }
  .envelope--back { top: 43px; height: 105px; background: var(--ink); }
  .envelope--back::before { content: ""; position: absolute; inset: 0 0 70px 0; background: linear-gradient(90deg, var(--blue-dark), var(--blue)); }
  .envelope--back .envelope__addr { position: absolute; right: 12px; top: 42px; font-size: 5px; line-height: 7px; color: #cccccc; text-align: right; }
  .envelope--flap { left: 804px; width: 372px; top: 108px; height: 80px; background: var(--flap); }
  .envelope--flap svg { position: absolute; inset: 0; }
  .envelope--front { top: 168px; height: 190px; background: var(--paper); }
  .envelope__band { height: 26px; background: var(--ink); display: flex; align-items: center; padding: 0 10px; font-size: 5px; color: #dddddd; }
  .envelope__strip { position: absolute; left: 0; right: 0; bottom: 0; height: 10px; background: linear-gradient(90deg, var(--blue-dark), var(--blue)); }

  .card { position: absolute; left: 768px; top: 368px; width: 404px; height: 112px; background: var(--ink); border-radius: 4px; display: flex; padding: 12px; gap: 12px; }
  .card__front { width: 120px; display: flex; flex-direction: column; align-items: center; justify-content: center; gap: 6px; }
  .card__front .brand { font-size: 10px; }
  .card__person { text-align: center; color: var(--paper); font-size: 6px; line-height: 8px; }
  .card__person strong { color: var(--blue); font-size: 7px; }
  .card__certs { font-size: 4.5px; color: #bbbbbb; text-align: center; }
  .card__codes { flex: 1; columns: 2; column-gap: 8px; font-size: 4px; line-height: 5.6px; color: #cccccc; border-left: 1px solid #444; padding-left: 10px; }
  .card__codes li { list-style: none; break-inside: avoid; }
  .card__accent { position: absolute; right: 12px; bottom: 12px; width: 22px; height: 22px; border-radius: 50%; background: var(--blue); }
</style>
</head>
<body>

<section class="sheet sheet--one" aria-label="Letterhead option 1">
  <header class="sheet__header">
    <div class="brand"><span class="brand__dot"></span>FARWELL GROUP</div>
    <div class="contact-mini">3620 E Tamsin Road<br>Orange, CA 92814<br>greta@farwellgrp.net</div>
  </header>
  <div class="watermark" role="img" aria-label="Faint city buildings and sunrise backdrop"></div>
  <footer class="sheet__footer">
    <span>3620 E Tamsin Road, Orange, CA 92814</span>
    <span>(714) 555-0142</span>
    <span>www.farwellgrp.net</span>
  </footer>
</section>

<section class="sheet sheet--two" aria-label="Fax cover option 2">
  <header class="sheet__header">
    <div class="brand"><span class="brand__dot"></span>FARWELL GROUP</div>
    <div class="contact-mini">3620 E Tamsin Road<br>Orange, CA 92814<br>(714) 555-0142</div>
  </header>
  <h1 class="fax__title">FAX</h1>
  <div class="fax__rule"></div>
  <div class="fax__fields">
    <span class="fax__field">To:</span><span class="fax__field">From:</span>
    <span class="fax__field">Fax:</span><span class="fax__field">Pages:</span>
    <span class="fax__field">Phone:</span><span class="fax__field">Date:</span>
    <span class="fax__field">Re:</span><span class="fax__field">CC:</span>
  </div>
  <div class="fax__checks">
    <span class="fax__check">Urgent</span>
    <span class="fax__check">For Review</span>
    <span class="fax__check">Please Comment</span>
    <span class="fax__check">Please Reply</span>
    <span class="fax__check">Please Recycle</span>
  </div>
  <div class="watermark" role="img" aria-label="Small faint city buildings backdrop"></div>
</section>

<p class="label label--one">option 1</p>
<p class="label label--two">option 2</p>

<div class="envelope envelope--back" aria-label="Envelope reverse">
  <div class="envelope__addr">Corporate Office<br>3620 E Tamsin Road<br>Orange, CA 92814</div>
</div>
<div class="envelope envelope--flap" aria-hidden="true">
  <svg width="372" height="80" viewBox="0 0 372 80"><polygon points="0,0 372,0 186,60" fill="#444444"/></svg>
</div>
<div class="envelope envelope--front" aria-label="Envelope front">
  <div class="envelope__band">3620 E Tamsin Road, Orange, CA 92814 &nbsp;|&nbsp; www.farwellgrp.net</div>
  <div class="envelope__strip"></div>
</div>

<article class="card" aria-label="Business card">
  <div class="card__front">
    <div class="brand"><span class="brand__dot"></span>FARWELL GROUP</div>
    <div class="card__person"><strong>Greta Volsky</strong><br>President<br>greta@farwellgrp.net<br>482650, K, D74</div>
    <div class="card__certs">*8(a) *SDB *SBE *MBE *DBE *CBE</div>
  </div>
  <ul class="card__codes">
    <li>221119 – Other Electric Power Generation</li>
    <li>236210 – Industrial Building Construction</li>
    <li>236220 – Commercial Building Construction</li>
    <li>237310 – Highway, Street, Bridge</li>
    <li>238160 – Roofing Contractors</li>
    <li>238170 – Siding Contractors</li>
    <li>238220 – Plumbing, Heating, A/C</li>
    <li>238310 – Drywall and Insulation</li>
    <li>238320 – Painting and Wall Covering</li>
    <li>238340 – Tile and Terrazzo</li>
    <li>238350 – Finish Carpentry</li>
    <li>238390 – Other Building Finishing</li>
    <li>238910 – Site Preparation</li>
    <li>238990 – Other Specialty Trade</li>
    <li>541350 – Building Inspection</li>
    <li>561210 – Facilities Support</li>
    <li>561790 – Other Services to Buildings</li>
  </ul>
  <span class="card__accent"></span>
</article>

</body>
</html>
```